VELINTA Promotions - Business Card Design Project

We are looking for a classy business cards for Promotion Company based in Larkmoor, Canada named Velinta Promotions.

Velinta Promotions has an idea and vision to set high standard, be EXCLUSIVE and attract a group of people that will follow us through events we promote (night clubs, brand promotions, music events, and sport events)

We want to present a high standards and classy image to the others...
Updates

Target Market(s)

male/female age 25-40 Target: business owners young entrepreneur - clubing industry - media industry - promotion industry - marketing media industry

Industry/Entity Type

Events

Requirements
Must have
• business cards should be classy, make people feel exclusive , make people react ..

```html
<!DOCTYPE html>
<html lang="en">
<head>
<meta charset="utf-8">
<title>Velinta Promotions — Business Card</title>
<link rel="stylesheet" href="https://fonts.googleapis.com/css2?family=Cinzel:wght@400;700&family=Arimo&display=swap">
<style>
  :root {
    --paper: #ffffff;
    --card: #0c0c0c;
    --accent: #22b5e3;
    --muted: #6d6d6d;
    --light: #e8e8e8;
    --note: #333333;
    --rule: #555555;
    --vine-a: #2a2a2a;
    --vine-b: #161616;
  }
  * { margin: 0; padding: 0; box-sizing: border-box; }
  html, body { width: 1200px; height: 900px; overflow: hidden; background: var(--paper); }
  .sheet { position: relative; width: 1200px; height: 900px; font-family: "Cinzel", serif; }

  .card { position: absolute; top: 316px; width: 236px; height: 374px; background: var(--card); overflow: hidden; }
  .card--front { left: 236px; border-top-left-radius: 28px; }
  .card--back { left: 666px; border-top-right-radius: 28px; }

  .vine-area {
    position: absolute; left: 0; top: 60px; width: 236px; height: 150px;
    background: radial-gradient(ellipse at 70% 45%, var(--vine-a), var(--vine-b) 70%, transparent 100%);
  }

  .wordmark { position: absolute; color: var(--accent); font-weight: 400; line-height: 1; white-space: nowrap; }
  .wordmark__name { display: block; font-size: 24px; letter-spacing: 1px; }
  .wordmark__sub { display: block; font-size: 8px; letter-spacing: 3px; margin-top: 3px; padding-left: 34px; }
  .card--front .wordmark { left: 20px; top: 298px; }
  .card--back .wordmark { left: 14px; top: 60px; }

  .contact { position: absolute; left: 34px; top: 168px; white-space: nowrap; }
  .contact__name { color: var(--light); font-size: 15px; line-height: 18px; letter-spacing: 4px; }
  .contact__role { color: var(--accent); font-size: 7px; line-height: 10px; letter-spacing: 2px; margin-top: 2px; }
  .contact__lines { list-style: none; margin-top: 32px; font-size: 10px; line-height: 14px; letter-spacing: 2.5px; }
  .contact__lines li { height: 26px; color: var(--muted); }
  .contact__lines .is-accent { color: var(--accent); }

  .note { position: absolute; font-family: "Arimo", sans-serif; font-size: 12px; line-height: 15px; color: var(--note); }
  .note--varnish { left: 504px; top: 256px; width: 120px; }
  .note--corner { left: 920px; top: 182px; width: 120px; }
  .side-label { position: absolute; top: 674px; font-family: "Arimo", sans-serif; font-size: 11px; color: var(--note); }
  .side-label--front { left: 478px; }
  .side-label--back { left: 908px; }
  .leaders { position: absolute; left: 0; top: 0; }
</style>
</head>
<body>
<main class="sheet">
  <svg class="leaders" width="1200" height="900" aria-hidden="true">
    <polyline points="500,264 492,264 492,410 474,410" fill="none" stroke="var(--rule)" stroke-width="1"/>
    <polyline points="916,190 908,190 908,326 890,326" fill="none" stroke="var(--rule)" stroke-width="1"/>
  </svg>

  <section class="card card--front">
    <div class="vine-area" role="img" aria-label="Subtle clear-varnish vine swirl decoration"></div>
    <div class="wordmark">
      <span class="wordmark__name">VELINTA</span>
      <span class="wordmark__sub">PROMOTIONS</span>
    </div>
  </section>
  <p class="note note--varnish">A subtle clear varnish for the vine design</p>
  <span class="side-label side-label--front">front</span>

  <section class="card card--back">
    <div class="wordmark">
      <span class="wordmark__name">VELINTA</span>
      <span class="wordmark__sub">PROMOTIONS</span>
    </div>
    <div class="contact">
      <p class="contact__name">MARIN DOLAK</p>
      <p class="contact__role">PROMOTION SPECIALISTS</p>
      <ul class="contact__lines">
        <li>2240 HARBOUR LANE</li>
        <li class="is-accent">LARKMOOR, CANADA</li>
        <li>(416) 555-0142</li>
        <li class="is-accent">MD@VELINTA.COM</li>
        <li>WWW.VELINTA.COM</li>
      </ul>
    </div>
  </section>
  <p class="note note--corner">.5 rounded corner to add a bit of uniqueness</p>
  <span class="side-label side-label--back">back</span>
</main>
</body>
</html>
```